Quarlwick Builders Business Cards

I want to use the logo and make an unique business card that shows the textured Logo with brick and builings. I want to be able to stand out when I pass out business cards.

```html
<!DOCTYPE html>
<html lang="en">
<head>
<meta charset="utf-8">
<title>Quarlwick Builders Business Cards</title>
<link rel="stylesheet" href="https://fonts.googleapis.com/css2?family=Saira:ital,wght@0,500;0,700;1,600;1,700&family=Saira+Condensed:wght@800&display=swap">
<style>
  :root {
    --stage: #151515;
    --card-dark: #1c1c1c;
    --wall-light: #3a3a3a;
    --wall-mid: #262626;
    --wall-deep: #0f0f0f;
    --brick-red-a: #ea5228;
    --brick-red-b: #b8361a;
    --brick-red-c: #7e2412;
    --accent: #f04a1c;
    --ink-light: #f4f4f4;
    --divider: #d9d9d9;
  }
  * { box-sizing: border-box; margin: 0; padding: 0; }
  html, body {
    width: 1200px; height: 963px; overflow: hidden;
    background: var(--stage);
    font-family: "Saira", sans-serif;
  }
  .card {
    position: absolute; left: 220px;
    width: 760px; height: 434px;
    overflow: hidden; border-radius: 4px;
    background: var(--card-dark);
    box-shadow: 0 12px 30px rgba(0,0,0,.6);
  }
  .card--front { top: 36px; }
  .card--back { top: 494px; }

  .wall-texture {
    position: absolute; inset: 0;
    background:
      radial-gradient(ellipse at 30% 25%, rgba(255,255,255,.07), transparent 60%),
      linear-gradient(150deg, var(--wall-light) 0%, var(--wall-mid) 45%, var(--wall-deep) 100%);
  }

  .brand {
    position: absolute; display: flex; align-items: center; gap: 12px;
    color: var(--accent);
    font-family: "Saira Condensed", sans-serif; font-weight: 800;
    text-transform: uppercase; letter-spacing: 1px; line-height: 1;
    white-space: nowrap;
  }
  .brand__mark { background: var(--accent); flex: none; }
  .card--front .brand { left: 40px; top: 128px; font-size: 36px; }
  .card--front .brand__mark { width: 24px; height: 24px; }
  .card--back .brand { left: 0; right: 0; top: 180px; justify-content: center; font-size: 68px; }
  .card--back .brand__mark { width: 46px; height: 46px; }

  .divider {
    position: absolute; left: 432px; top: 40px;
    width: 2px; height: 250px; background: var(--divider);
  }
  .contact { position: absolute; left: 462px; top: 52px; color: var(--ink-light); }
  .contact__name {
    font-family: "Saira Condensed", sans-serif; font-weight: 800;
    color: var(--accent); font-size: 40px; line-height: 1; letter-spacing: 1px;
    text-transform: uppercase;
  }
  .contact__role { font-style: italic; font-weight: 600; font-size: 20px; margin-top: 6px; }
  .contact__address { font-weight: 700; font-size: 19px; line-height: 1.3; margin-top: 18px; }
  .contact__list { list-style: none; margin-top: 16px; }
  .contact__item {
    display: flex; align-items: center; gap: 10px;
    font-weight: 700; font-size: 19px; line-height: 1.55;
  }
  .contact__icon { width: 16px; height: 16px; flex: none; }

  .service-band {
    position: absolute; left: 0; right: 0; bottom: 0; height: 104px;
    background: linear-gradient(180deg, var(--brick-red-a) 0%, var(--brick-red-b) 55%, var(--brick-red-c) 100%);
    border-top: 3px solid var(--brick-red-c);
  }
  .service-band__list {
    position: absolute; left: 0; right: 0; top: 20px;
    display: flex; justify-content: center; gap: 18px; list-style: none;
    color: var(--ink-light); font-weight: 700; font-style: italic;
    font-size: 20px; text-transform: uppercase; letter-spacing: .5px;
  }
  .service-band__list li { display: flex; align-items: center; gap: 8px; }
  .service-band__list li::before {
    content: ""; width: 8px; height: 8px; border-radius: 50%; background: var(--ink-light);
  }
</style>
</head>
<body>

<section class="card card--front">
  <div class="wall-texture" role="img" aria-label="Dark charcoal brick wall texture"></div>

  <div class="brand"><span class="brand__mark"></span>Quarlwick Builders</div>

  <div class="divider"></div>

  <div class="contact">
    <h1 class="contact__name">Daniel Harrow</h1>
    <p class="contact__role">Managing Director</p>
    <p class="contact__address">Your Address, City<br>State, Zip 0000</p>
    <ul class="contact__list">
      <li class="contact__item">
        <svg class="contact__icon" viewBox="0 0 16 16"><circle cx="8" cy="8" r="8" fill="#f04a1c"/><path d="M5 4l2 0 1 2-1 1a5 5 0 0 0 2 2l1-1 2 1 0 2c-4 0-7-3-7-7z" fill="#1c1c1c"/></svg>
        044-555 010 274
      </li>
      <li class="contact__item">
        <svg class="contact__icon" viewBox="0 0 16 16"><circle cx="8" cy="8" r="8" fill="#f04a1c"/><rect x="4" y="5" width="8" height="6" fill="#1c1c1c"/><path d="M4 5l4 3 4-3" stroke="#f04a1c" fill="none"/></svg>
        info@quarlwick.com
      </li>
      <li class="contact__item">
        <svg class="contact__icon" viewBox="0 0 16 16"><circle cx="8" cy="8" r="8" fill="#f04a1c"/><circle cx="8" cy="8" r="4.5" fill="none" stroke="#1c1c1c" stroke-width="1.3"/><path d="M3.5 8h9M8 3.5c-2 2-2 7 0 9M8 3.5c2 2 2 7 0 9" stroke="#1c1c1c" fill="none"/></svg>
        www.quarlwickbuild.com
      </li>
    </ul>
  </div>

  <div class="service-band" role="img" aria-label="Red brick wall strip listing services">
    <ul class="service-band__list">
      <li>Patios</li>
      <li>Sidewalks</li>
      <li>Retaining Walls</li>
      <li>Foundations</li>
    </ul>
  </div>
</section>

<section class="card card--back">
  <div class="wall-texture" role="img" aria-label="Dark charcoal brick wall texture"></div>
  <div class="brand"><span class="brand__mark"></span>Quarlwick Builders</div>
</section>

</body>
</html>
```